I want a minimal signage design for my pool service company.

Design a premium modern lower-door decal/wrap for a graphite Varnak Delmo dual cab ute.
The design should look tough, clean and high-end. Think factory/OEM style graphics rather than a typical tradie signwriting setup.
Style:
* Modern and aggressive
* Minimal but eye-catching
* Fluro/electric blue accents
* Suit graphite grey paint
* Motorsport / Kestin Volgar inspired
* Premium marine/pool industry feel
Placement:
* Runs across the lower section of both doors
* Can slightly extend toward rear tray/front guard
* Must flow nicely with the shape of the ute
Include:
* Brindlewood Pool Care logo
* 0431 572 183
Avoid:
* Big rectangular blocks
* Cheap-looking wrap styles
* Too much text
* Overly busy graphics
The design should look professional enough that it could suit a high-end branded company vehicle while still standing out on the road.
Needs to be a ai/pdf/svg file and dimensions will be about 1600mm x 200mm
Pool service

```html
<!DOCTYPE html>
<html lang="en">
<head>
<meta charset="utf-8">
<title>Brindlewood Pool Care – Lower Door Decal</title>
<link href="https://fonts.googleapis.com/css2?family=Oswald:wght@700&display=swap" rel="stylesheet">
<style>
  :root {
    --bg: #f4f5f7;
    --navy: #141656;
    --sky: #5aa6dc;
    --white: #ffffff;
  }
  html, body {
    margin: 0;
    padding: 0;
    width: 1200px;
    height: 417px;
    overflow: hidden;
    background: var(--bg);
  }
  .decal {
    display: block;
    width: 1200px;
    height: 417px;
  }
  .decal__stripe { fill: var(--white); }
  .decal__band { fill: var(--navy); }
  .decal__accent { fill: var(--sky); }
  .decal__phone-panel { fill: var(--white); }
  .logo-mark {
    fill: var(--sky);
    stroke: var(--navy);
    stroke-width: 8;
  }
  .brand-name {
    font-family: "Oswald", sans-serif;
    font-weight: 700;
    font-size: 46px;
    fill: var(--white);
    letter-spacing: -0.5px;
  }
  .phone-number {
    font-family: "Oswald", sans-serif;
    font-weight: 700;
    font-size: 46px;
    fill: var(--navy);
    letter-spacing: 1px;
  }
</style>
</head>
<body>
  <svg class="decal" viewBox="0 0 1200 417" xmlns="http://www.w3.org/2000/svg" aria-label="Brindlewood Pool Care lower door decal">
    <!-- thin top stripe -->
    <polygon class="decal__stripe" points="30,160 1180,136 1180,146 30,170"/>
    <!-- main navy band -->
    <path class="decal__band" d="M30,170 L1180,146 L1180,262 L80,276 Q40,276 34,240 Z"/>
    <!-- lower accent stripe -->
    <path class="decal__accent" d="M40,268 L1180,254 L1180,282 L1150,300 L90,306 Q52,306 40,268 Z"/>
    <!-- phone panel with accent frame -->
    <polygon class="decal__accent" points="610,194 1180,184 1180,262 572,270"/>
    <polygon class="decal__phone-panel" points="628,206 1160,198 1160,252 596,258"/>

    <!-- brand mark placeholder sitting on the stripe -->
    <circle class="logo-mark" cx="400" cy="140" r="38" role="img" aria-label="Brindlewood Pool Care brand mark"/>

    <text class="brand-name" x="70" y="256">Brindlewood Pool Care</text>
    <text class="phone-number" x="660" y="246">0431 572 183</text>
  </svg>
</body>
</html>
```